Global Weight loss program

we need a business card based in Brooklyn , NY called ZestwellPRO . Mara Tullin Opdegard the founder and creator of ZestwellPRO Movement. A business based around nutrition, health, Whole Foods and fitness.

Industry/Entity Type

Food Service

Contact Information for Business Card

Phone number : 718-402-3859
website www.zestwellpro.example
email : mara@zestwellpro.example

Font styles to use
Sans Serif

Requirements
Must have
• logo colors
• green black and gold
Nice to have
• must be simple and sharp.
Should not have
• pictures of items

```html
<!DOCTYPE html>
<html lang="en">
<head>
<meta charset="utf-8">
<title>ZestwellPRO Business Card</title>
<link rel="stylesheet" href="https://fonts.googleapis.com/css2?family=Open+Sans:wght@400;600&display=swap">
<style>
  :root {
    --backdrop: #232427;
    --card: #231f20;
    --green-light: #8dc63f;
    --green-mid: #4eae47;
    --green-deep: #0e9247;
    --name-green: #2eaa4a;
    --white: #ffffff;
    --muted: #cfcfcf;
  }
  * { margin: 0; padding: 0; box-sizing: border-box; }
  html, body { width: 1200px; height: 960px; overflow: hidden; }
  body {
    background: var(--backdrop);
    font-family: "Open Sans", Arial, sans-serif;
    position: relative;
  }
  .card {
    position: absolute;
    width: 640px;
    height: 366px;
    background: var(--card);
    overflow: hidden;
    box-shadow: 0 18px 40px rgba(0,0,0,0.45);
  }
  .card--front { left: 80px; top: 70px; }
  .card--back { left: 480px; top: 524px; }

  .brand-art {
    position: absolute;
    top: 0;
    height: 100%;
    background: linear-gradient(135deg, var(--green-light) 0%, var(--green-mid) 55%, var(--green-deep) 100%);
  }
  .card--front .brand-art { right: 0; width: 250px; }
  .card--back .brand-art { left: 0; width: 210px; }

  .wordmark {
    position: absolute;
    color: var(--white);
  }
  .wordmark__name {
    display: block;
    font-weight: 400;
    font-size: 46px;
    line-height: 1;
    letter-spacing: -0.5px;
  }
  .wordmark__tagline {
    display: block;
    font-size: 11.5px;
    letter-spacing: 2px;
    color: var(--muted);
    margin-top: 4px;
    margin-left: 4px;
  }
  .card--front .wordmark { left: 90px; top: 196px; }
  .card--back .wordmark { left: 236px; top: 270px; }

  .holder {
    position: absolute;
    right: 40px;
    top: 40px;
    text-align: left;
  }
  .holder__name {
    color: var(--name-green);
    font-size: 24px;
    font-weight: 400;
    letter-spacing: -0.5px;
  }
  .holder__role {
    color: var(--white);
    font-size: 14px;
    margin-top: 2px;
  }

  .contacts {
    position: absolute;
    right: 40px;
    top: 178px;
    list-style: none;
  }
  .contacts li {
    display: flex;
    align-items: center;
    gap: 10px;
    color: var(--white);
    font-size: 15px;
    line-height: 28px;
  }
  .contacts svg { width: 14px; height: 14px; fill: var(--name-green); flex: none; }
</style>
</head>
<body>

<section class="card card--front" aria-label="Card front">
  <div class="brand-art" role="img" aria-label="Large green brand letter with a figure holding an apple"></div>
  <div class="wordmark">
    <span class="wordmark__name">ZestwellPRO</span>
    <span class="wordmark__tagline">Fitness, Nutrition and Health</span>
  </div>
</section>

<section class="card card--back" aria-label="Card back">
  <div class="brand-art" role="img" aria-label="Large green brand letter with a stretching figure silhouette"></div>

  <div class="holder">
    <p class="holder__name">Mara Tullin Opdegard</p>
    <p class="holder__role">Founder</p>
  </div>

  <ul class="contacts">
    <li>
      <svg viewBox="0 0 24 24" aria-hidden="true"><path d="M6.6 10.8a15.1 15.1 0 0 0 6.6 6.6l2.2-2.2a1 1 0 0 1 1-.25 11.4 11.4 0 0 0 3.6.57 1 1 0 0 1 1 1V20a1 1 0 0 1-1 1A17 17 0 0 1 3 4a1 1 0 0 1 1-1h3.5a1 1 0 0 1 1 1c0 1.25.2 2.45.57 3.6a1 1 0 0 1-.25 1z"/></svg>
      718-402-3859
    </li>
    <li>
      <svg viewBox="0 0 24 24" aria-hidden="true"><path d="M2 5h20v14H2zm2 2v.5l8 5 8-5V7zm0 2.8V17h16V9.8l-8 5z"/></svg>
      mara@zestwellpro.example
    </li>
    <li>
      <svg viewBox="0 0 24 24" aria-hidden="true"><path d="M12 2a10 10 0 1 0 0 20 10 10 0 0 0 0-20zm0 2c.9 0 2.2 2 2.7 5H9.3C9.8 6 11.1 4 12 4zM4.3 11h3a17 17 0 0 0 0 2h-3a8 8 0 0 1 0-2zm5 0h5.4a15 15 0 0 1 0 2H9.3a15 15 0 0 1 0-2zm7.4 0h3a8 8 0 0 1 0 2h-3a17 17 0 0 0 0-2zM9.3 15h5.4c-.5 3-1.8 5-2.7 5s-2.2-2-2.7-5z"/></svg>
      www.zestwellpro.example
    </li>
  </ul>

  <div class="wordmark">
    <span class="wordmark__name">ZestwellPRO</span>
    <span class="wordmark__tagline">Fitness, Nutrition and Health</span>
  </div>
</section>

</body>
</html>
```